Letterhead Design Project

I need letterhead designed for my law firm. It would also be used for web based stuff as well.

Industry/Entity Type

Law Firm

```html
<!DOCTYPE html>
<html lang="en">
<head>
<meta charset="utf-8">
<title>Hartwell &amp; Voss Letterhead</title>
<link href="https://fonts.googleapis.com/css2?family=Marcellus&display=swap" rel="stylesheet">
<style>
  :root {
    --backdrop: #ffffff;
    --paper: #f1f1f1;
    --band: #000000;
    --band-text: #ffffff;
    --ink: #111111;
  }
  * { margin: 0; padding: 0; box-sizing: border-box; }
  html, body {
    width: 1200px;
    height: 1000px;
    overflow: hidden;
    background: var(--backdrop);
  }
  .letterhead {
    position: absolute;
    left: 264px;
    top: 69px;
    width: 658px;
    height: 852px;
    background: var(--paper);
    font-family: "Marcellus", serif;
  }
  .header-band {
    position: absolute;
    left: 0;
    top: 37px;
    width: 100%;
    height: 60px;
    background: var(--band);
    display: flex;
    align-items: center;
    justify-content: center;
  }
  .firm-name {
    color: var(--band-text);
    font-size: 34px;
    font-weight: 400;
    letter-spacing: 0.5px;
    line-height: 1;
    padding-top: 4px;
  }
  .firm-tagline {
    position: absolute;
    top: 102px;
    width: 100%;
    text-align: center;
    color: var(--ink);
    font-size: 15px;
    letter-spacing: 3px;
  }
  .footer-band {
    position: absolute;
    left: 0;
    top: 808px;
    width: 100%;
    height: 29px;
    background: var(--band);
    display: flex;
    align-items: center;
    justify-content: center;
    gap: 20px;
    color: var(--band-text);
    font-size: 10.5px;
    letter-spacing: 0.2px;
    text-transform: uppercase;
  }
</style>
</head>
<body>
  <main class="letterhead">
    <header class="header-band">
      <h1 class="firm-name">HARTWELL &amp; VOSS</h1>
    </header>
    <p class="firm-tagline">LAW FIRM</p>
    <footer class="footer-band">
      <span class="footer-name">Hartwell &amp; Voss Law Firm</span>
      <span class="footer-address">482 Maple Ave. City, CA 90210</span>
      <span class="footer-phone">555-010-4477</span>
      <span class="footer-email">office@hartwellvoss.com</span>
    </footer>
  </main>
</body>
</html>
```